This book will apply the 12 Steps to gaming addiction, also known as video game addiction. The primary purpose of the book is to provide an effective solution for this new type of addiction. The solution is based on the rich and successful concepts of traditional twelve-step programs like RL.

The title on the cover will be "Nine Doors Past the Glowing Screen" and "by Martin Quorby". A subtitle can be used if it works in your design of "A Practical Path Beyond Compulsive Console Play". Cover will be for a 6" x 9" book approximately 110 pages in length.

Some back cover text including some review quotes and an author bio are in the attached Word doc. There is also an author photo attached for for the back cover.

Requirements
Must have
• For the cover design it could be stylized, or an image, a partial image, or whatever. I am open to suggestions. Think about what would be noticed by a person searching for help with moderating their video game use, or by the parents or loved ones of problem gamers. Something contemporary and eye catching.

```html
<!DOCTYPE html>
<html lang="en">
<head>
<meta charset="utf-8">
<title>Nine Doors Past the Glowing Screen — Cover Spread</title>
<link rel="stylesheet" href="https://fonts.googleapis.com/css2?family=Bebas+Neue&family=Marcellus&family=Montserrat:ital,wght@0,300;0,400;0,500;1,400;1,500&display=swap">
<style>
  :root {
    --paper: #ffffff;
    --ink: #1d1d1f;
    --title-blue: #5b5cf0;
    --title-red: #e8564c;
    --navy: #1b1585;
    --rule-orange: #e6a23c;
    --reserve-grey: #48484c;
    --art-pale: #eceefd;
    --art-light: #c9cdf8;
    --art-mid: #8d94f4;
    --art-deep: #5a5be8;
    --photo-warm: #7a5a44;
    --photo-dark: #2f2a2a;
  }
  * { margin: 0; padding: 0; box-sizing: border-box; }
  html, body { width: 1200px; height: 900px; overflow: hidden; background: var(--paper); }
  .spread { position: relative; width: 1200px; height: 900px; background: var(--paper); color: var(--ink); }

  /* Back cover */
  .back { position: absolute; left: 0; top: 0; width: 580px; height: 900px; font-family: "Montserrat", sans-serif; }
  .praise-heading { position: absolute; left: 22px; top: 44px; width: 530px; text-align: center; font-size: 15px; font-weight: 500; letter-spacing: -0.1px; }
  .praise-list { position: absolute; left: 22px; top: 78px; width: 536px; }
  .praise { font-size: 12px; line-height: 15.2px; font-style: italic; letter-spacing: -0.25px; margin-bottom: 11px; }
  .praise cite { display: block; font-style: italic; font-weight: 500; }
  .praise-rule { position: absolute; left: 120px; top: 335px; width: 300px; height: 1.5px; background: var(--rule-orange); }
  .blurb { position: absolute; left: 22px; top: 342px; width: 536px; font-size: 14px; line-height: 15.3px; font-weight: 300; letter-spacing: -0.25px; }
  .blurb p { margin-bottom: 10px; }
  .author-photo { position: absolute; left: 22px; top: 620px; width: 134px; height: 122px; background: linear-gradient(160deg, var(--photo-warm), var(--photo-dark)); }
  .author-heading { position: absolute; left: 174px; top: 606px; width: 380px; text-align: center; font-size: 21px; font-weight: 400; letter-spacing: 0.2px; }
  .author-bio { position: absolute; left: 174px; top: 640px; width: 382px; font-size: 12.4px; line-height: 15.2px; font-weight: 300; letter-spacing: -0.2px; }
  .author-bio em { font-weight: 500; }
  .code-reserve { position: absolute; left: 354px; top: 749px; width: 199px; height: 120px; background: var(--reserve-grey); }

  /* Spine */
  .spine { position: absolute; left: 578px; top: 0; width: 44px; height: 900px; font-family: "Bebas Neue", sans-serif; }
  .spine-title { position: absolute; left: 6px; top: 58px; writing-mode: vertical-rl; font-size: 33px; line-height: 33px; color: var(--ink); letter-spacing: 0.2px; }
  .spine-title .accent { color: var(--title-red); }
  .spine-author { position: absolute; left: 6px; top: 704px; writing-mode: vertical-rl; font-size: 36px; line-height: 33px; color: var(--ink); }

  /* Front cover */
  .front { position: absolute; left: 622px; top: 0; width: 578px; height: 900px; }
  .title { position: absolute; left: 90px; top: 60px; font-family: "Bebas Neue", sans-serif; text-transform: uppercase; color: var(--title-blue); line-height: 0.86; }
  .title-line { display: block; white-space: nowrap; }
  .title-small { font-size: 48px; }
  .title-big { font-size: 94px; }
  .title-red { font-size: 132px; color: var(--title-red); }
  .subtitle { position: absolute; left: 60px; top: 370px; width: 460px; text-align: center; font-family: "Marcellus", serif; font-size: 30px; line-height: 40px; color: var(--navy); }
  .cover-art {
    position: absolute; left: 100px; top: 446px; width: 380px; height: 360px; border-radius: 28px;
    background: linear-gradient(180deg, var(--art-pale) 0%, var(--art-light) 22%, var(--art-mid) 50%, var(--art-deep) 78%, var(--art-light) 100%);
  }
  .front-author { position: absolute; left: 0; top: 808px; width: 578px; text-align: center; font-family: "Bebas Neue", sans-serif; font-size: 66px; line-height: 66px; color: var(--navy); letter-spacing: 0.5px; }
</style>
</head>
<body>
<main class="spread">

  <section class="back">
    <h2 class="praise-heading">Praise for Nine Doors Past the Glowing Screen</h2>
    <div class="praise-list">
      <blockquote class="praise">“A must-read for anyone who is addicted to or thinks they may have a problem with digital gaming. This eloquent work will also be useful to academics and clinicians exploring potential solutions. The author recognizes the similarities between gaming addiction and other addictions, and logically applies one of the most effective known solutions for addiction - The Twelve Steps.”
        <cite>-- Dale Brennick, Noted Interventionist and Keynote Speaker</cite></blockquote>
      <blockquote class="praise">“If you suffer from digital gaming addiction, I strongly encourage you to use this book as your road map to get you back to the real world.”
        <cite>-- Owen Calloway, Founder of Signal Street Review.</cite></blockquote>
      <blockquote class="praise">“As a high school teacher for 24 years, husband, father, coach, and 12-Step member, I can assure you that this book will transform the life of anyone who is addicted to video games. Well written, easy to understand, and a wonderful book that will provide you with a clear road map to recovery, and this includes teenagers, a group I have been working with in the classroom for decades.”
        <cite>-- Luis Ortega, Harbor Vale, OR High School Teacher.</cite></blockquote>
    </div>
    <div class="praise-rule"></div>
    <div class="blurb">
      <p>An effective solution to the challenge of Digital Gaming Addiction (aka Video Game Addiction) based on the rich and successful tradition of the Twelve Steps.</p>
      <p>Addiction to Digital Gaming is a new and troubling phenomenon that has burst upon an unprepared society with alarming speed. Many people crave the use of Digital Games in a strikingly similar way to any other addict. Digital Games are a complex software and hardware system that have been designed to promote continued and progressive usage. This sophisticated technology clearly feeds on natural addictive tendencies.</p>
      <p>The 12 Steps are one of the most effective methods for treating addiction in human history. Originating with Recovery League in 1939, the 12 Steps have since been used to treat a variety of other addictions, including drugs, sex, gambling, eating disorders, and many others. Now in this groundbreaking work the 12 Steps are applied to the complex and evolving contemporary phenomenon of Digital Gaming Addiction.</p>
    </div>
    <div class="author-photo" role="img" aria-label="Author portrait photograph"></div>
    <h3 class="author-heading">MARTIN QUORBY</h3>
    <p class="author-bio"><em>Marty Quorby</em> is a Technology Consultant and Writer with many years of professional coding and consulting experience. He also struggled with addiction to drugs and alcohol and is now clean and sober in a Twelve-Step program for over 17 years. This unique combination of 12-Step experience and technology expertise led him to create Nine Doors Past the Glowing Screen.</p>
    <div class="code-reserve"></div>
  </section>

  <section class="spine">
    <div class="spine-title">NINE DOORS PAST THE GLOWING <span class="accent">SCREEN</span></div>
    <div class="spine-author">MARTIN QUORBY</div>
  </section>

  <section class="front">
    <h1 class="title">
      <span class="title-line title-small">Nine</span>
      <span class="title-line title-big">Doors Past</span>
      <span class="title-line"><span class="title-small">The </span><span class="title-big">Glowing</span></span>
      <span class="title-line title-red">Screen</span>
    </h1>
    <p class="subtitle">A Practical Path Beyond Compulsive Console Play</p>
    <div class="cover-art" role="img" aria-label="Illustration of people using phones and a laptop around a large web browser screen in front of a globe, with small app icons floating nearby"></div>
    <div class="front-author">MARTIN QUORBY</div>
  </section>

</main>
</body>
</html>
```